Webdesign for an Health & Beauty Center

We need a new modern and elegant web design for the relaunch of the http://veskarin.at/ website.
The website is for a company which offer all services for a beuty center like epilation, cosmetics and more.
The new website should use big emotional background images and a modern menu.
All in all the website should give a female expression and the design should be clear and not playful.
The existing logo used be used for the new design, the base colours of the existing website could be used optionally.

Reason: Review of the designs together with the customer needs a little more time.

Industry/Entity Type
It Company
Look and feel
Each slider illustrates characteristics of the customer's brand and the style your logo design should communicate.

```html
<!DOCTYPE html>
<html lang="en">
<head>
<meta charset="utf-8">
<title>Veskarin – Health &amp; Beauty Center</title>
<link href="https://fonts.googleapis.com/css2?family=Open+Sans:ital,wght@0,400;0,600;0,700;1,600&family=PT+Sans:wght@400;700&display=swap" rel="stylesheet">
<style>
  :root {
    --tan: #a58a6c;
    --tan-light: #b89d7f;
    --cream: #f7f1ea;
    --ink: #1a1a1a;
    --dark-brown: #2b1f17;
    --band-top: #4a3526;
    --band-bottom: #5a4030;
    --footer: #000000;
    --white: #ffffff;
  }
  * { box-sizing: border-box; margin: 0; padding: 0; }
  html, body { width: 1200px; height: 960px; overflow: hidden; background: var(--white); }
  body { position: relative; font-family: "PT Sans", sans-serif; color: var(--ink); }

  .site-header { position: absolute; left: 0; top: 0; width: 1200px; height: 118px; background: var(--white); }
  .brand { position: absolute; left: 144px; top: 14px; display: flex; align-items: center; gap: 8px; }
  .brand-dot { width: 14px; height: 14px; border-radius: 50%; background: var(--tan-light); }
  .brand-name { font-family: "PT Sans", sans-serif; font-size: 34px; font-weight: 400; letter-spacing: 3px; color: var(--tan-light); }

  .social { position: absolute; left: 907px; top: 8px; display: flex; gap: 4px; }
  .social span { width: 23px; height: 23px; border-radius: 4px; background: var(--tan); display: block; }

  .search { position: absolute; left: 794px; top: 79px; display: flex; gap: 7px; }
  .search-input { width: 187px; height: 27px; border: 1px solid #d6d6d6; border-radius: 3px; background: linear-gradient(#f1f1f1, #fff); }
  .search-button { width: 67px; height: 27px; border-radius: 2px; background: var(--tan); color: var(--white); font-size: 13px; line-height: 27px; text-align: center; }

  .main-nav { position: absolute; left: 136px; top: 83px; display: flex; height: 26px; }
  .main-nav a { display: block; padding: 0 9px; font-size: 15px; line-height: 26px; color: var(--ink); text-decoration: none; text-transform: uppercase; }
  .main-nav a.is-active { background: var(--tan); }
  .header-rule { position: absolute; left: 0; top: 114px; width: 1200px; height: 4px; background: var(--tan); }

  .hero { position: absolute; left: 0; top: 118px; width: 1200px; height: 590px;
    background:
      radial-gradient(ellipse 520px 420px at 940px 260px, #e3b89a 0%, rgba(227,184,154,0) 70%),
      radial-gradient(ellipse 700px 300px at 420px 330px, #d9a47f 0%, rgba(217,164,127,0) 75%),
      linear-gradient(180deg, #f6ede4 0%, #efd9c6 25%, #dcae8c 55%, #c98f6b 78%, #a9745a 90%, #d9b59c 100%); }

  .dropdown { position: absolute; left: 307px; top: 132px; width: 199px; height: 130px; background: var(--tan); border-radius: 10px; padding: 10px 15px; }
  .dropdown::before { content: ""; position: absolute; left: 86px; top: -14px; border: 14px solid transparent; border-top: 0; border-bottom-color: var(--tan); }
  .dropdown a { display: block; height: 26px; line-height: 26px; text-align: center; color: var(--white); font-size: 15px; text-decoration: none; border-top: 1px solid rgba(255,255,255,0.25); }
  .dropdown a:first-child { border-top: 0; }

  .appointment { position: absolute; left: 195px; top: 515px; width: 450px; }
  .appointment h1 { font-family: "Open Sans", sans-serif; font-weight: 700; font-size: 43px; line-height: 56px; letter-spacing: -1px; color: var(--white); text-shadow: 2px 3px 3px rgba(0,0,0,0.45); white-space: nowrap; }
  .appointment h1 .accent { color: var(--dark-brown); text-shadow: 2px 3px 3px rgba(0,0,0,0.3); }
  .appointment .tagline { text-align: right; font-family: "Open Sans", sans-serif; font-weight: 600; font-size: 22px; line-height: 26px; color: var(--white); text-shadow: 1px 1px 2px rgba(0,0,0,0.4); }
  .appointment .tagline .accent { color: var(--dark-brown); text-shadow: none; }
  .appointment-form { position: absolute; left: 195px; top: 602px; display: flex; gap: 5px; }
  .field { height: 37px; background: var(--white); font-family: "Open Sans", sans-serif; font-size: 12px; color: #666; line-height: 37px; padding-left: 11px; }
  .field-name { width: 168px; }
  .field-cell { width: 142px; padding-left: 13px; }
  .send { width: 131px; height: 37px; margin-left: 1px; background: var(--tan); color: var(--white); font-family: "Open Sans", sans-serif; font-weight: 700; font-size: 17px; line-height: 37px; text-align: center; }

  .features { position: absolute; left: 0; top: 706px; width: 1200px; height: 212px;
    background: linear-gradient(180deg, var(--band-top) 0%, #3d2c20 40%, var(--band-bottom) 100%);
    border-top: 6px solid var(--tan); }
  .features::before { content: ""; position: absolute; left: 592px; top: 0; border: 8px solid transparent; border-top-color: var(--tan); border-bottom: 0; border-width: 12px 8px 0; }
  .feature { position: absolute; top: 25px; }
  .feature-head { display: flex; align-items: center; gap: 9px; height: 42px; }
  .feature-head h2 { font-family: "Open Sans", sans-serif; font-weight: 700; font-size: 16px; color: var(--white); text-shadow: 1px 1px 2px rgba(0,0,0,0.6); }
  .feature p { margin-top: 4px; font-family: "Open Sans", sans-serif; font-style: italic; font-weight: 600; font-size: 12.3px; line-height: 23.4px; color: var(--white); }
  .feature-sustain { left: 168px; width: 240px; }
  .feature-health { left: 480px; width: 290px; }
  .feature-careers { left: 820px; width: 220px; }
  .feature-careers p { margin-top: 8px; }

  .site-footer { position: absolute; left: 0; top: 918px; width: 1200px; height: 42px; background: var(--footer); }
  .site-footer .copyright { position: absolute; right: 148px; top: 0; line-height: 42px; font-family: "Open Sans", sans-serif; font-weight: 700; font-size: 14px; color: var(--white); }
</style>
</head>
<body>
  <header class="site-header">
    <div class="brand"><span class="brand-dot"></span><span class="brand-name">veskarin</span></div>
    <div class="social"><span></span><span></span><span></span><span></span><span></span></div>
    <nav class="main-nav">
      <a href="#">Home</a><a href="#">Promotions</a><a href="#">Location</a><a href="#" class="is-active">Services</a><a href="#">Price Lists</a><a href="#">Gallery</a><a href="#">Contact Us</a>
    </nav>
    <div class="search"><div class="search-input"></div><div class="search-button">Search</div></div>
    <div class="header-rule"></div>
  </header>

  <div class="hero" role="img" aria-label="Photo of a woman relaxing on a spa table, her reflection in calm water below"></div>

  <div class="dropdown">
    <a href="#">LOREM IPSUM</a><a href="#">LOREM IPSUM IS DUMMY</a><a href="#">LOREM IPSUM</a><a href="#">LOREM IPSUM IS DUMMY</a>
  </div>

  <section class="appointment">
    <h1>Make An <span class="accent">Appointment</span></h1>
    <p class="tagline">We <span class="accent">Care</span> For You...</p>
  </section>
  <div class="appointment-form">
    <div class="field field-name">Name</div>
    <div class="field field-cell">Cell #</div>
    <div class="send">Send</div>
  </div>

  <section class="features">
    <div class="feature feature-sustain">
      <div class="feature-head">
        <svg width="46" height="42" viewBox="0 0 46 42" aria-hidden="true"><g fill="none" stroke="#a58a6c" stroke-width="6"><path d="M14 32 L6 32 L14 18"/><path d="M17 10 L23 4 L30 16"/><path d="M34 22 L40 32 L26 34"/></g><g fill="#a58a6c"><path d="M10 14 l10 2 -6 8z"/><path d="M32 10 l2 10 -9 -3z"/><path d="M24 28 l0 10 -8 -5z"/></g></svg>
        <h2>Sustainability</h2>
      </div>
      <p>Phasellus a purus justo, at ornare orci. Sed odio risus, auctor quis eleifend eget, mollis id metus. Maecenas vehicula ultrices eros, eget commodo quam pulvinar interdum. Integer ac massa</p>
    </div>
    <div class="feature feature-health">
      <div class="feature-head">
        <svg width="44" height="44" viewBox="0 0 44 44" aria-hidden="true"><g fill="#a58a6c"><circle cx="22" cy="22" r="15"/><rect x="19" y="1" width="6" height="42"/><rect x="1" y="19" width="42" height="6"/><rect x="19" y="1" width="6" height="42" transform="rotate(45 22 22)"/><rect x="19" y="1" width="6" height="42" transform="rotate(-45 22 22)"/></g><circle cx="22" cy="22" r="9" fill="#3d2c20"/><path d="M22 16v12M16 22h12" stroke="#a58a6c" stroke-width="3.5"/></svg>
        <h2>Health, Safety &amp; Environment</h2>
      </div>
      <p>Phasellus a purus justo, at ornare orci. Sed odio risus, auctor quis eleifend eget, mollis id metus. Maecenas vehicula ultrices eros, eget commodo quam pulvinar interdum. Integer ac massa ipsum, at porta ipsum.</p>
    </div>
    <div class="feature feature-careers">
      <div class="feature-head">
        <svg width="40" height="46" viewBox="0 0 40 46" aria-hidden="true"><g fill="none" stroke="#a58a6c" stroke-width="2.5"><path d="M8 3h20l9 9v30H8z"/><path d="M28 3v9h9"/><path d="M14 16h14M14 22h18M14 28h18"/><rect x="1" y="31" width="20" height="13" fill="#3d2c20"/></g><text x="3" y="42" font-family="Open Sans, sans-serif" font-size="11" font-weight="700" fill="#a58a6c">CV</text></svg>
        <h2>Careers</h2>
      </div>
      <p>Phasellus a purus justo, at ornare orci. Sed odio risus, auctor quis eleifend eget, mollis id metus. Maecenas vehicula ultrices eros, eget commodo quam pulvinar interdum. Integer ac</p>
    </div>
  </section>

  <footer class="site-footer">
    <span class="copyright">Copyright 2014 All Right Reserved</span>
  </footer>
</body>
</html>
```